Car rental website design for a UAE car rental company

This project is about creating a new website design for a car rental company located in Dubai (United Arab Emirates), I opened the same project a few months ago but I didn't receive a lot of appealing entries so I closed it but this time I am marking the project as guaranteed to avoid such situation again, if you have already provided a design before then please re-submit again on this project so that it is considered while reviewing all the designs

A few important things:

1- We need a simple non-complex design
2- The final deliverable would be 2 screens (PSD, JPEG ... etc), the first screen is for the home page and the second screen is for an internal page
3- The home page must have a section that end users can use to rent a car online directly from the home page instead of going into some inner pages
4- The current website is very old and not very appealing so avoid creating a similar design (www.quarvin-drive.example)
5- The name is Quarvin but the company rents normal cars (no Limousin cars will be rented) so avoid adding any fancy cars in the images/graphics used in the design, just normal end users cars
6- The expected pages would be: home, About us, Our team, Strategy, Contact us and links to social media pages
7- The attachments include the company's logo and some screens from other car rental companies that provide online rentals/payments

If you have any questions please feel free to ask and please note that we will need the designs urgently

Thanks

Target Market(s)

Dubai - United Arab Emirates

Industry/Entity Type

It Company

Number of Pages Required

2 page

Font styles to use
Sans Serif

Requirements
Must have
• Check the project details
Nice to have
Should not have

```html
<!DOCTYPE html>
<html lang="en">
<head>
<meta charset="utf-8">
<title>Quarvin Rent A Car</title>
<link href="https://fonts.googleapis.com/css2?family=Arvo:wght@400;700&family=Courier+Prime:wght@400;700&display=swap" rel="stylesheet">
<style>
:root{
  --crimson:#a30034;
  --crimson-band:rgba(170,20,60,.82);
  --grey-text:#8a8f8c;
  --body-text:#7a7a80;
  --white:#ffffff;
  --ink:#1c1c1c;
}
*{box-sizing:border-box;margin:0;padding:0}
html,body{width:1200px;height:1031px;overflow:hidden;background:var(--white)}
body{position:relative;font-family:"Arvo",serif;color:var(--ink)}
.topbar{position:absolute;left:0;top:0;width:1200px;height:28px;background:var(--crimson)}
.topbar .phone{position:absolute;left:676px;top:5px;display:flex;align-items:center;gap:8px;color:#f3d6de;font-family:"Courier Prime",monospace;font-size:15px;letter-spacing:1px}
.topbar .social{position:absolute;left:866px;top:6px;display:flex;gap:14px}
.topbar .social span{width:16px;height:16px;border-radius:50%;background:var(--white);display:block}
.brand{position:absolute;left:180px;top:72px;display:flex;align-items:center;gap:10px}
.brand .mark{width:34px;height:34px;background:var(--crimson)}
.brand .name{font-size:30px;color:var(--grey-text);font-weight:400}
.book-now{position:absolute;left:798px;top:41px;width:199px;height:40px;background:var(--crimson);color:var(--white);border-radius:6px;font-size:17px;display:flex;align-items:center;justify-content:center;text-decoration:none}
.nav{position:absolute;top:106px;left:0;font-family:"Courier Prime",monospace;font-size:16px}
.nav a{position:absolute;white-space:nowrap;color:var(--grey-text);text-decoration:none;letter-spacing:1px}
.nav a.active{color:var(--crimson);font-weight:700}
.nav .underline{position:absolute;left:444px;top:47px;width:59px;height:2px;background:var(--crimson)}
.hero{position:absolute;left:0;top:155px;width:1200px;height:565px;background:linear-gradient(180deg,#6d6c63 0%,#8a8274 30%,#7b7166 50%,#6a6350 75%,#4f4a36 100%)}
.hero h1{position:absolute;left:0;top:60px;width:1200px;text-align:center;font-size:60px;font-weight:400;color:var(--white)}
.hero h1 em{font-style:normal;color:var(--crimson)}
.hero .tagline{position:absolute;left:0;top:138px;width:1200px;text-align:center;font-size:20px;color:var(--white)}
.booking{position:absolute;left:0;top:365px;width:1200px;height:226px;background:var(--crimson-band)}
.field-label{position:absolute;color:var(--white);font-size:15px}
.select,.input{position:absolute;height:20px;background:linear-gradient(#f2f2f2,#fff);font-family:"Courier Prime",monospace;font-weight:700;font-size:12px;padding-left:10px;line-height:20px;color:#222}
.select::after{content:"⇕";position:absolute;right:8px;top:0;color:#777;font-size:12px}
.icon{position:absolute}
.btn-outline{position:absolute;height:45px;border:1px solid var(--white);color:var(--white);font-size:16px;display:flex;align-items:center;justify-content:center;gap:20px}
.welcome h2{position:absolute;left:188px;top:813px;font-size:26px;color:var(--crimson);font-weight:400}
.welcome p{position:absolute;left:190px;top:856px;width:380px;font-size:12px;line-height:15.5px;color:var(--body-text)}
.read-more{position:absolute;left:188px;top:928px;width:160px;height:37px;background:var(--crimson);color:var(--white);border-radius:4px;font-size:15px;display:flex;align-items:center;justify-content:center;text-decoration:none}
.car-photo{position:absolute;left:615px;top:795px;width:455px;height:225px;border-radius:120px 140px 40px 40px;background:radial-gradient(ellipse at 55% 45%,#3a3a3c 0%,#141414 60%,#e8e8e8 100%)}
</style>
</head>
<body>
<div class="topbar">
  <div class="phone">
    <svg width="12" height="20" viewBox="0 0 12 20"><rect x="1" y="1" width="10" height="18" rx="2" fill="none" stroke="#f3d6de" stroke-width="1.5"/><circle cx="6" cy="16" r="1" fill="#f3d6de"/></svg>
    +971 45550123
  </div>
  <div class="social"><span></span><span></span><span></span><span></span><span></span></div>
</div>

<div class="brand"><span class="mark"></span><span class="name">Quarvin</span></div>
<a class="book-now" href="#">BOOK NOW</a>

<nav class="nav">
  <a class="active" style="left:452px">Home</a>
  <a style="left:539px">About us</a>
  <a style="left:661px">Our Team</a>
  <a style="left:776px">Strategy</a>
  <a style="left:882px">Contact Us</a>
  <span class="underline"></span>
</nav>

<section class="hero" role="img" aria-label="Desert mountain road with a white sedan driving">
  <h1>Experience An <em>Extra Mile</em></h1>
  <p class="tagline">Of Comfort,pleasure And Leisure From The Best</p>
</section>

<form class="booking">
  <span class="field-label" style="left:188px;top:20px">Pick up Location</span>
  <svg class="icon" style="left:543px;top:13px" width="15" height="22" viewBox="0 0 15 22"><path d="M7.5 0a7.5 7.5 0 0 0-7.5 7.5C0 13 7.5 22 7.5 22S15 13 15 7.5A7.5 7.5 0 0 0 7.5 0z" fill="#fff"/><circle cx="7.5" cy="7.5" r="3" fill="#a30034"/></svg>
  <div class="select" style="left:186px;top:46px;width:379px">Select</div>

  <span class="field-label" style="left:635px;top:20px">Return Location</span>
  <svg class="icon" style="left:991px;top:13px" width="15" height="22" viewBox="0 0 15 22"><path d="M7.5 0a7.5 7.5 0 0 0-7.5 7.5C0 13 7.5 22 7.5 22S15 13 15 7.5A7.5 7.5 0 0 0 7.5 0z" fill="#fff"/><circle cx="7.5" cy="7.5" r="3" fill="#a30034"/></svg>
  <div class="select" style="left:634px;top:46px;width:379px">Select</div>

  <span class="field-label" style="left:188px;top:90px">Pick up Date &amp; Time</span>
  <svg class="icon" style="left:449px;top:94px" width="20" height="20" viewBox="0 0 20 20"><rect x="1" y="3" width="18" height="16" fill="none" stroke="#fff" stroke-width="1.5"/><rect x="1" y="3" width="18" height="4" fill="#fff"/><text x="10" y="17" font-size="8" fill="#fff" text-anchor="middle" font-family="Arial, sans-serif">27</text></svg>
  <svg class="icon" style="left:544px;top:95px" width="20" height="20" viewBox="0 0 20 20"><circle cx="10" cy="10" r="9" fill="#fff"/><path d="M10 4v6l4 3" stroke="#a30034" stroke-width="1.5" fill="none"/></svg>
  <div class="input" style="left:186px;top:122px;width:183px"></div>
  <div class="select" style="left:377px;top:122px;width:92px;text-align:center;padding:0 18px 0 0;font-weight:400">00</div>
  <div class="select" style="left:475px;top:122px;width:91px;text-align:center;padding:0 18px 0 0;font-weight:400">00</div>

  <span class="field-label" style="left:635px;top:95px">Return Date &amp; Time</span>
  <svg class="icon" style="left:896px;top:94px" width="20" height="20" viewBox="0 0 20 20"><rect x="1" y="3" width="18" height="16" fill="none" stroke="#fff" stroke-width="1.5"/><rect x="1" y="3" width="18" height="4" fill="#fff"/><text x="10" y="17" font-size="8" fill="#fff" text-anchor="middle" font-family="Arial, sans-serif">27</text></svg>
  <svg class="icon" style="left:991px;top:95px" width="20" height="20" viewBox="0 0 20 20"><circle cx="10" cy="10" r="9" fill="#fff"/><path d="M10 4v6l4 3" stroke="#a30034" stroke-width="1.5" fill="none"/></svg>
  <div class="input" style="left:634px;top:125px;width:183px"></div>
  <div class="select" style="left:825px;top:125px;width:91px;text-align:center;padding:0 18px 0 0;font-weight:400">00</div>
  <div class="select" style="left:922px;top:125px;width:91px;text-align:center;padding:0 18px 0 0;font-weight:400">00</div>

  <span class="field-label" style="left:189px;top:160px">Vechicle Type</span>
  <div class="select" style="left:187px;top:187px;width:379px">Show All Vechile</div>

  <div class="btn-outline" style="left:634px;top:174px;width:182px">GET A QUOTE
    <svg width="24" height="18" viewBox="0 0 24 18"><path d="M1 9h20M13 2l8 7-8 7" stroke="#fff" stroke-width="3" fill="none"/></svg>
  </div>
  <div class="btn-outline" style="left:832px;top:175px;width:181px">Worldwide booking</div>
</form>

<section class="welcome">
  <h2>WELCOME TO QUARVIN</h2>
  <p>As Dubai is expected to welcome millions of tourists and visitors, car rental industry is believed to escalate more rapidly in the region.</p>
  <a class="read-more" href="#">Read more</a>
  <div class="car-photo" role="img" aria-label="Black sedan car, three-quarter front view"></div>
</section>
</body>
</html>
```